Brightfernrx website

We are a weight loss clinic and we need a website built. please look at these websites for content and style. Just need like 5 pages see samples. AI files of logo are not avail yet so use sample for place set

https://glowshiftstudio.com/
ortanvital.com
https://pinecrestclinicalbodybalance.com/
https://yourslimmingnook.com/
https://qrvskinstudio.com/treatments/weight-loss-injections/

Target Market(s)

Women

Industry/Entity Type

weight loss

Coding

Coded - Design and coding required

Number of Pages Required

5+ page

Requirements
Nice to have
• please make look like a medspa website

```html
<!DOCTYPE html>
<html lang="en">
<head>
<meta charset="utf-8">
<title>Brightfernrx – Womens Weightloss Clinic</title>
<link href="https://fonts.googleapis.com/css2?family=Gentium+Book+Plus:ital,wght@0,400;0,700;1,400&family=Montserrat:wght@400;500;600&display=swap" rel="stylesheet">
<style>
:root{
  --blue:#3d95cf;
  --green:#7cb342;
  --ink:#222;
  --muted:#555;
  --line:#e5e5e5;
  --white:#fff;
}
*{box-sizing:border-box;margin:0;padding:0}
html,body{width:1200px;height:4464px;overflow:hidden}
body{position:relative;font-family:"Montserrat",sans-serif;color:var(--ink);background:var(--white)}
.serif{font-family:"Gentium Book Plus",serif}
.abs{position:absolute}
.center{text-align:center;left:0;width:1200px}
.btn{position:absolute;display:flex;align-items:center;justify-content:center;gap:8px;color:#fff;font-size:14px;font-weight:500}
.btn-blue{background:var(--blue)}
.btn-green{background:var(--green);border-radius:24px}
.ph{position:absolute}

/* nav */
.brand{position:absolute;display:flex;align-items:center;gap:8px;font-family:"Gentium Book Plus",serif;font-size:26px;color:var(--blue)}
.brand i{display:block;width:30px;height:30px;border-radius:50%;background:var(--green)}
.nav{position:absolute;top:26px;left:522px;display:flex;gap:28px;font-size:12px;color:#333}
.nav .on{color:var(--green);position:relative}
.nav .on:after{content:"";position:absolute;left:8px;top:22px;width:16px;height:2px;background:var(--green)}
.nav-cta{position:absolute;left:860px;top:19px;width:182px;height:34px;border:2px solid var(--blue);color:var(--blue);font-size:12px;display:flex;align-items:center;justify-content:center}

/* hero */
.hero{left:0;top:0;width:1200px;height:576px;background:linear-gradient(90deg,#d9d4cd 0%,#c9c4bf 45%,#b8a99a 70%,#d2c7bb 100%)}
.hero h1{position:absolute;left:160px;top:180px;font-family:"Gentium Book Plus",serif;font-style:italic;font-weight:400;font-size:52px;line-height:58px;color:#1c1c1c}
.hero p{position:absolute;left:161px;top:312px;width:430px;font-size:12.5px;line-height:25px;color:#333}

/* features */
.feature{position:absolute;top:576px;width:274px;height:182px;background:#fff;box-shadow:0 6px 16px rgba(0,0,0,.08);text-align:center}
.feature svg{margin-top:16px}
.feature h3{font-family:"Gentium Book Plus",serif;font-size:20px;font-weight:700;margin-top:10px;letter-spacing:.3px}
.feature p{font-size:12.5px;line-height:22px;color:var(--muted);margin:12px 24px 0}

/* headings */
.eyebrow{font-size:16px;letter-spacing:4px;color:#333}
.h-blue{font-family:"Gentium Book Plus",serif;color:var(--blue);font-size:31px}
.body-text{font-size:14.5px;line-height:30px;color:#333}

/* service cards */
.svc{position:absolute;width:274px;height:307px}
.svc .photo{position:absolute;left:0;top:0;width:274px;height:167px}
.svc .box{position:absolute;left:9px;top:167px;width:256px;height:140px;background:#fff;box-shadow:0 4px 14px rgba(0,0,0,.08);text-align:center}
.svc h4{font-size:16.5px;font-weight:500;margin-top:20px}
.svc p{font-size:12.5px;line-height:22px;color:var(--muted);margin-top:30px}
.svc .more{font-size:12.5px;color:var(--blue);margin-top:6px}
.svc.raised .photo{height:142px}
.svc.raised .box{top:142px;height:165px}

/* band */
.band{left:0;top:2168px;width:1200px;height:432px;background:linear-gradient(180deg,#3b7fb3 0%,#2f8fa0 60%,#2a9c8a 100%)}
.band h2{position:absolute;left:548px;top:64px;font-family:"Gentium Book Plus",serif;font-size:40px;line-height:50px;color:#fff;font-weight:400}
.band .sub{position:absolute;left:548px;top:176px;font-size:22px;color:#fff;font-weight:500}
.band .txt{position:absolute;left:548px;top:218px;width:500px;font-size:14.5px;line-height:30px;color:#e9f3f6}

/* results */
.ba{position:absolute;border-radius:22px;overflow:hidden}
.arrow{position:absolute;width:32px;height:32px;border-radius:50%;display:flex;align-items:center;justify-content:center}
.dots{position:absolute;display:flex;gap:6px}
.dots i{display:block;width:5px;height:5px;border-radius:50%;background:#ccc}
.dots i.on{background:var(--green)}

/* testimonials */
.quote{position:absolute;top:3231px;width:278px;height:270px;border:1px solid var(--line);border-radius:6px;background:#fff;text-align:center}
.stars{color:#f4b400;font-size:19px;letter-spacing:2px;margin-top:28px}
.quote p{font-size:12px;line-height:22px;color:#444;margin:10px 30px 0}
.quote hr{border:0;border-top:1px dashed #ccc;margin:16px 14px 0}
.quote .name{font-size:16px;font-weight:500;margin-top:16px}

/* location */
.location{left:0;top:3615px;width:1200px;height:498px;background:linear-gradient(135deg,#5f8f3c 0%,#6f9c46 50%,#5a8a38 100%)}
.location h2{position:absolute;left:735px;top:92px;font-family:"Gentium Book Plus",serif;font-size:34px;color:#fff;font-weight:400}
.loc-row{position:absolute;left:732px;display:flex;gap:14px;color:#fff;font-size:14.5px;line-height:24px}

/* footer */
.newsletter-title{font-family:"Gentium Book Plus",serif;color:var(--blue);font-size:20px}
.email{position:absolute;left:436px;top:4204px;width:300px;height:36px;border:1px solid var(--line);border-radius:18px;font-size:11px;color:#888;display:flex;align-items:center;padding-left:12px}
.submit{position:absolute;left:643px;top:4204px;width:94px;height:36px;border-radius:18px;background:#222;color:#fff;font-size:14px;display:flex;align-items:center;justify-content:center}
.copy{font-size:11.5px;color:#444}
</style>
</head>
<body>

<!-- HERO -->
<div class="ph hero" role="img" aria-label="Woman in a black bikini holding a sheer scarf on a sunny beach">
  <h1>Beautiful Results.<br>Beautiful You.</h1>
  <p>It is a long established fact that a reader will be distracted by the readable content of a page when looking at its layout.</p>
</div>
<div class="brand" style="left:160px;top:14px"><i></i>Brightfernrx</div>
<nav class="nav"><span class="on">About</span><span>Our Services</span><span>Blogs</span><span>Contact Us</span></nav>
<div class="nav-cta">Book An Appointment</div>
<div class="btn btn-blue" style="left:161px;top:386px;width:181px;height:36px;font-size:12px">Book An Appointment</div>

<!-- FEATURES -->
<div class="feature" style="left:160px">
  <svg width="44" height="50" viewBox="0 0 44 50" fill="none" stroke="#333" stroke-width="1.6"><circle cx="28" cy="14" r="11" stroke="var(--blue)"/><path d="M28 8v12M25 11h5a2 2 0 010 4h-4a2 2 0 000 4h5" stroke="var(--blue)"/><path d="M4 30h8v16H4zM12 32l10-4h8a3 3 0 010 6h-6M12 44l14 2 14-10-3-3-10 6"/></svg>
  <h3>Affordable for Anyone</h3>
  <p>Lorem ipsum dolor sit amet, cons ectetuer adipiscing elit..</p>
</div>
<div class="feature" style="left:463px">
  <svg width="44" height="50" viewBox="0 0 44 50" fill="none" stroke="#333" stroke-width="1.6"><rect x="6" y="6" width="32" height="40" rx="2"/><rect x="15" y="2" width="14" height="7" rx="1"/><circle cx="22" cy="20" r="5" stroke="var(--blue)"/><path d="M22 18v4M20 20h4M12 32h20M12 38h20" stroke="var(--blue)"/></svg>
  <h3>Doctor Prescribed</h3>
  <p>Lorem ipsum dolor sit amet, cons ectetuer adipiscing elit..</p>
</div>
<div class="feature" style="left:766px">
  <svg width="50" height="50" viewBox="0 0 50 50" fill="none" stroke="#333" stroke-width="1.6"><circle cx="25" cy="25" r="15" stroke-dasharray="4 3"/><circle cx="25" cy="20" r="5" stroke="var(--blue)"/><path d="M16 34c2-6 16-6 18 0" stroke="var(--blue)"/><circle cx="25" cy="5" r="3"/><circle cx="45" cy="25" r="3"/><circle cx="5" cy="25" r="3"/><circle cx="25" cy="45" r="3"/></svg>
  <h3>Supportive Staff</h3>
  <p>Lorem ipsum dolor sit amet, cons ectetuer adipiscing elit..</p>
</div>

<!-- ABOUT -->
<div class="abs center eyebrow" style="top:830px">ABOUT US</div>
<div class="abs center h-blue" style="top:856px">Reaching Your Weight Loss Goal</div>
<div class="abs center serif" style="top:896px;font-size:31px;font-weight:700">Is Definitely Doable!</div>
<div class="abs center body-text" style="top:944px;padding:0 240px">Lorem ipsum dolor sit amet, consectetuer adipiscing elit, sed diam nonummy nibh euismod tincidunt ut laoreet dolore magna aliquam erat volutpat. Ut wisi enim ad minim veniam, quis nostrud exerci tation ullamcorper suscipit lobortis nisl ut aliquip ex ea commodo consequat Lorem ipsum dolor sit amet, consectetuer adipiscing elit...</div>
<div class="btn btn-green" style="left:527px;top:1079px;width:147px;height:38px">Read More
  <svg width="16" height="10" viewBox="0 0 16 10" fill="none" stroke="#fff" stroke-width="1.6"><path d="M0 5h14M10 1l4 4-4 4"/></svg></div>

<!-- SERVICES -->
<div class="abs center h-blue" style="top:1274px">Our Services</div>
<div class="abs center body-text" style="top:1350px;padding:0 290px;font-size:14.5px;line-height:26px">Lorem ipsum dolor sit amet, consectetuer adipiscing elit, sed diam nonummy nibh euismod tincidunt ut laoreet dolore magna aliquam erat volutpat. Ut..</div>

<div class="svc" style="left:160px;top:1427px">
  <div class="photo" role="img" aria-label="Clinician measuring a client's waist in a bright office" style="background:linear-gradient(135deg,#d9d2c8,#a9a39b)"></div>
  <div class="box"><h4>Weight Loss</h4><p>Lorem ipsum dolor sit amet,<br>cons ectetuer adipiscing..</p></div>
</div>
<div class="svc raised" style="left:463px;top:1427px">
  <div class="photo" role="img" aria-label="Doctor consulting with a patient in an orange sweater" style="background:linear-gradient(135deg,#e8e3dc,#d28f5a)"></div>
  <div class="box"><h4>Medical Weight Loss</h4><p>Lorem ipsum dolor sit amet,<br>cons ectetuer adipiscing..</p><div class="more">Read More →</div></div>
</div>
<div class="svc" style="left:766px;top:1427px">
  <div class="photo" role="img" aria-label="Doctor holding an apple next to a measuring tape" style="background:linear-gradient(135deg,#eeeeee,#c8c8c8)"></div>
  <div class="box"><h4>Weight Loss Clinic</h4><p>Lorem ipsum dolor sit amet,<br>cons ectetuer adipiscing..</p></div>
</div>
<div class="svc" style="left:160px;top:1760px">
  <div class="photo" role="img" aria-label="Measuring tape wrapped around a waist" style="background:linear-gradient(135deg,#cfcfcf,#3c3c3c)"></div>
  <div class="box"><h4>Weight Loss Medications</h4><p>Lorem ipsum dolor sit amet,<br>cons ectetuer adipiscing..</p></div>
</div>
<div class="svc" style="left:463px;top:1760px">
  <div class="photo" role="img" aria-label="Doctor and patient talking in a clinic room" style="background:linear-gradient(135deg,#cfd6d2,#8f9a95)"></div>
  <div class="box"><h4>Weight Loss Consultations</h4><p>Lorem ipsum dolor sit amet,<br>cons ectetuer adipiscing..</p></div>
</div>
<div class="svc" style="left:766px;top:1760px">
  <div class="photo" role="img" aria-label="Woman measuring her waist with a yellow tape" style="background:linear-gradient(135deg,#b9b9b5,#6b6a4e)"></div>
  <div class="box"><h4>Weight Loss Programs</h4><p>Lorem ipsum dolor sit amet,<br>cons ectetuer adipiscing..</p></div>
</div>

<!-- BAND -->
<div class="ph band">
  <div class="ph" role="img" aria-label="Smiling woman in activewear with a slim waist" style="left:150px;top:0;width:320px;height:432px;background:linear-gradient(180deg,rgba(90,80,80,.3),rgba(40,40,50,.5))"></div>
  <h2>Start Your Weight-Loss<br>Journey Today</h2>
  <div class="sub">No Dieting. No Exercise. Just Results.</div>
  <div class="txt">Lorem ipsum dolor sit amet, consectetuer adipiscing elit, sed diam nonummy nibh euismod tincidunt ut laoreet..</div>
</div>
<div class="btn btn-green" style="left:546px;top:2473px;width:261px;height:42px;font-size:14.5px">
  <svg width="16" height="16" viewBox="0 0 16 16" fill="none" stroke="#fff" stroke-width="1.4"><rect x="1" y="3" width="14" height="12" rx="1"/><path d="M1 7h14M5 1v4M11 1v4"/></svg>Book An Appointment
  <svg width="16" height="10" viewBox="0 0 16 10" fill="none" stroke="#fff" stroke-width="1.6"><path d="M0 5h14M10 1l4 4-4 4"/></svg></div>

<!-- RESULTS -->
<div class="abs center h-blue" style="top:2670px">Beautiful Results. Beautiful You.</div>
<div class="ba" role="img" aria-label="Before and after side profile photos" style="left:160px;top:2788px;width:250px;height:180px;background:linear-gradient(90deg,#dfe6ee,#c9d6e4);opacity:.6"></div>
<div class="ba" role="img" aria-label="Before and after front photos of a woman" style="left:443px;top:2762px;width:316px;height:230px;background:linear-gradient(90deg,#d6d2cf 0%,#bdb6b1 49.7%,#fff 49.7%,#fff 50.3%,#d6d2cf 50.3%,#bdb6b1 100%);box-shadow:0 4px 18px rgba(0,0,0,.1)"></div>
<div class="ba" role="img" aria-label="Before and after full body photos" style="left:790px;top:2788px;width:250px;height:180px;background:linear-gradient(90deg,#e3dfdc,#d0cac6);opacity:.6"></div>
<div class="arrow" style="left:374px;top:2858px;background:#fff;box-shadow:0 2px 6px rgba(0,0,0,.15)"><svg width="10" height="10" viewBox="0 0 10 10"><path d="M7 1L2 5l5 4z" fill="#999"/></svg></div>
<div class="arrow" style="left:790px;top:2858px;background:var(--blue)"><svg width="10" height="10" viewBox="0 0 10 10"><path d="M3 1l5 4-5 4z" fill="#fff"/></svg></div>
<div class="dots" style="left:578px;top:3024px"><i></i><i class="on"></i><i></i><i></i></div>

<!-- TESTIMONIALS -->
<div class="abs center h-blue" style="top:3142px">Our Happy Member</div>
<div class="quote" style="left:161px"><div class="stars">★★★★★</div><p>"Lorem Pools has a wonderful team of real specialists. Last week they have built our new dream pool. We have been very impressed by their project manager and professional work teams. Thanks for super"</p><hr><div class="name">Maya Ellison</div></div>
<div class="quote" style="left:462px"><div class="stars">★★★★★</div><p>"Lorem Pools has a wonderful team of real specialists. Last week they have built our new dream pool. We have been very impressed by their project manager and professional work teams. Thanks for super"</p><hr><div class="name">Dana Whitfield</div></div>
<div class="quote" style="left:763px"><div class="stars">★★★★★</div><p>"Lorem Pools has a wonderful team of real specialists. Last week they have built our new dream pool. We have been very impressed by their project manager and professional work teams. Thanks for super"</p><hr><div class="name">Rosa Vance</div></div>
<div class="arrow" style="left:95px;top:3350px;background:#fff;box-shadow:0 2px 6px rgba(0,0,0,.15)"><svg width="10" height="10" viewBox="0 0 10 10"><path d="M7 1L2 5l5 4z" fill="#999"/></svg></div>
<div class="arrow" style="left:1073px;top:3350px;background:var(--blue)"><svg width="10" height="10" viewBox="0 0 10 10"><path d="M3 1l5 4-5 4z" fill="#fff"/></svg></div>
<div class="dots" style="left:583px;top:3532px"><i></i><i class="on"></i><i></i><i></i></div>

<!-- LOCATION -->
<div class="ph location">
  <div class="ph" role="img" aria-label="Faint map of the United States with clinic location marker" style="left:160px;top:80px;width:460px;height:320px;background:radial-gradient(ellipse at center,rgba(180,200,140,.45),rgba(95,143,60,0) 70%)"></div>
  <div class="ph" style="left:378px;top:102px;width:88px;height:88px;border-radius:50%;background:#fff"></div>
  <div class="abs serif" style="left:478px;top:120px;color:#fff;font-size:17px;line-height:24px">Brightfernrx Womens<br>Weightloss Clinic</div>
  <h2>Location Map</h2>
  <div class="loc-row" style="top:176px"><svg width="30" height="30" viewBox="0 0 30 30" fill="none" stroke="#fff" stroke-width="1.4"><circle cx="14" cy="16" r="11"/><path d="M3 16h22M14 5c-5 6-5 16 0 22M14 5c5 6 5 16 0 22"/><path d="M24 2a4 4 0 014 4c0 3-4 7-4 7s-4-4-4-7a4 4 0 014-4z" fill="#5f8f3c"/></svg><div>2250 Saltmarsh Lane Suite<br>401 Harbor Point, FL 33000</div></div>
  <div class="loc-row" style="top:246px"><svg width="30" height="30" viewBox="0 0 30 30" fill="none" stroke="#fff" stroke-width="1.4"><path d="M6 4l5 1 2 6-3 2c1 3 4 6 7 7l2-3 6 2 1 5c-10 2-22-10-20-20z"/><path d="M18 4a8 8 0 018 8M18 8a4 4 0 014 4"/></svg><div>Phone<br>(555)010-2468</div></div>
  <div class="loc-row" style="top:312px"><svg width="30" height="30" viewBox="0 0 30 30" fill="none" stroke="#fff" stroke-width="1.4"><rect x="2" y="10" width="26" height="17"/><path d="M2 10l13 10 13-10M7 13V3h16v10M11 8h8"/></svg><div>Email<br>info@brightfernrx.com</div></div>
</div>

<!-- FOOTER -->
<div class="brand" style="left:160px;top:4184px"><i></i>Brightfernrx</div>
<div class="abs newsletter-title" style="left:445px;top:4167px">Newsletter Sign up</div>
<div class="email">Enter Your Email Address</div>
<div class="submit">Submit</div>
<div class="btn btn-green" style="left:790px;top:4188px;width:243px;height:40px;font-size:14px">
  <svg width="16" height="16" viewBox="0 0 16 16" fill="none" stroke="#fff" stroke-width="1.4"><rect x="1" y="3" width="14" height="12" rx="1"/><path d="M1 7h14M5 1v4M11 1v4"/></svg>Book An Appointment
  <svg width="16" height="10" viewBox="0 0 16 10" fill="none" stroke="#fff" stroke-width="1.6"><path d="M0 5h14M10 1l4 4-4 4"/></svg></div>
<div class="abs center copy" style="top:4300px">© 2023 Brightfernrx Womens Weightloss Clinic. All Right Reserved</div>
<div class="ph" role="img" aria-label="Woman in a blue bikini and sun hat lying on the sand" style="left:380px;top:4326px;width:440px;height:138px;background:radial-gradient(ellipse at 50% 80%,#e8c9b0 0%,#f3e4d6 50%,rgba(255,255,255,0) 75%)"></div>

</body>
</html>
```